Bright Pelvic Health Business Card

Need a business card for a surgical practice called Bright Pelvic Health. We have recently selected a logo (attached). The business card will need to have two formats:
1) One with the logo/physician name/ contact info on the front and location information on the back.
2) One in "appointment reminder card" style with the logo/ contact info/ date/ time on the front and the location information on the back.

The front side should include the following information:
- Logo
- Rohan K. Desai, MD FACOG
- phone: 469-555-0172
- fax: 1-469-555-0188
- email: admin@brightpelvic.example
- website: www.brightpelvichealth.example

The back side should have the office locations listed:
4815 Juniper Way, Plano, TX 75093
3720 Baywood Rd, Plano, TX 75025
2245 Larkspur Ln, Irving, TX 75038
815 W Finch St S310, Dallas, TX 75201
3516 Quarry Blvd, Grand Prairie, TX 75051
6437 Wexley Crest Dr, San Antonio, TX 78240
5822 Ember Rd, Pasadena, TX 77504

Target Market(s)

1. Other physicians who might refer patients
2. Female patients

Industry/Entity Type

Business

Font styles to use
Other font styles liked:
• Tahoma for lettering

Requirements
Must have
• As per the instructions
Should not have
• No other images needed -- please try to keep font consistent with logo design. Can use Tahoma as the font for lettering.

```html
<!DOCTYPE html>
<html lang="en">
<head>
<meta charset="utf-8">
<title>Bright Pelvic Health Business Cards</title>
<link href="https://fonts.googleapis.com/css2?family=PT+Sans:wght@400;700&display=swap" rel="stylesheet">
<style>
  :root {
    --navy: #1f5ea6;
    --teal: #4ab3c8;
    --ink: #111111;
    --card-top: #ffffff;
    --card-bottom: #e9e9ea;
    --mark-soft: #e2e8f2;
    --mark-text: #d6dfed;
    --page: #ffffff;
  }
  * { margin: 0; padding: 0; box-sizing: border-box; }
  html, body { width: 1200px; height: 900px; overflow: hidden; background: var(--page); }
  body { position: relative; font-family: "PT Sans", Tahoma, sans-serif; color: var(--navy); }

  .brand {
    position: absolute; display: flex; align-items: center; justify-content: center; gap: 10px;
    color: var(--navy); font-weight: 700; white-space: nowrap;
  }
  .brand-dot { border-radius: 50%; background: var(--navy); flex: none; }
  .brand--hero { left: 0; width: 1200px; top: 185px; font-size: 32px; }
  .brand--hero .brand-dot { width: 16px; height: 16px; }
  .brand--card { left: 0; width: 100%; font-size: 15px; gap: 6px; }
  .brand--card .brand-dot { width: 9px; height: 9px; }

  .card {
    position: absolute; top: 312px; width: 249px; height: 436px;
    background: linear-gradient(to bottom, var(--card-top) 35%, var(--card-bottom));
    box-shadow: 4px 10px 16px rgba(0,0,0,0.22);
  }
  .card--front-doctor { left: 25px; }
  .card--back-doctor { left: 318px; }
  .card--front-reminder { left: 640px; }
  .card--back-reminder { left: 922px; }

  .watermark {
    position: absolute; left: 0; top: 56px; width: 100%; height: 170px;
    display: flex; flex-direction: column; align-items: center;
  }
  .watermark-dot { width: 128px; height: 128px; border-radius: 50%; background: var(--mark-soft); }
  .watermark-name { margin-top: 14px; font-size: 22px; font-weight: 700; color: var(--mark-text); white-space: nowrap; }

  .locations { position: absolute; left: 0; width: 100%; top: 278px; text-align: center; font-size: 10.5px; line-height: 17.8px; list-style: none; }
  .locations li:nth-child(odd) { color: var(--navy); }
  .locations li:nth-child(even) { color: var(--teal); }

  .physician { position: absolute; left: 19px; top: 252px; }
  .physician-name { font-size: 19px; font-weight: 700; letter-spacing: 0.8px; color: var(--navy); }
  .physician-title { font-size: 13px; font-weight: 700; letter-spacing: 1px; color: var(--teal); margin-top: 6px; }

  .contact { position: absolute; font-size: 12.5px; line-height: 22px; list-style: none; }
  .contact .label { color: var(--teal); }
  .contact .value { color: var(--navy); }
  .contact .gap { margin-top: 4px; }
  .card--front-doctor .contact { left: 19px; top: 318px; }
  .card--front-reminder .contact { left: 0; width: 100%; top: 328px; text-align: center; }

  .appointment { position: absolute; left: 37px; top: 224px; list-style: none; }
  .appointment li { display: flex; align-items: flex-end; font-size: 13.5px; font-weight: 700; height: 32px; }
  .appointment li:first-child { color: var(--teal); }
  .appointment li:last-child { color: var(--navy); }
  .appointment .fill-line { width: 134px; border-bottom: 1px dotted var(--navy); margin: 0 0 4px 4px; }
  .appointment li:last-child .fill-line { width: 130px; }

  .caption { position: absolute; top: 822px; font-size: 18px; color: var(--ink); letter-spacing: 1.4px; white-space: nowrap; }
  .caption--business { left: 129px; }
  .caption--reminder { left: 648px; }
</style>
</head>
<body>

  <div class="brand brand--hero"><span class="brand-dot"></span>Bright Pelvic Health</div>

  <section class="card card--front-doctor">
    <div class="brand brand--card" style="top:88px"><span class="brand-dot"></span>Bright Pelvic Health</div>
    <div class="physician">
      <p class="physician-name">Rohan K. Desai,</p>
      <p class="physician-title">MD FACOG</p>
    </div>
    <ul class="contact">
      <li><span class="label">phone:</span> <span class="value">469-555-0172</span></li>
      <li><span class="label">fax:</span> <span class="value">1-469-555-0188</span></li>
      <li class="gap"><span class="label">email:</span> <span class="value">admin@brightpelvic.example</span></li>
      <li><span class="label">website:</span> <span class="value">www.brightpelvichealth.example</span></li>
    </ul>
  </section>

  <section class="card card--back-doctor">
    <div class="watermark" role="img" aria-label="Faint brand mark decoration">
      <span class="watermark-dot"></span>
      <span class="watermark-name">Bright Pelvic Health</span>
    </div>
    <ul class="locations">
      <li>4815 Juniper Way, Plano, TX 75093</li>
      <li>3720 Baywood Rd, Plano, TX 75025</li>
      <li>2245 Larkspur Ln, Irving, TX 75038</li>
      <li>815 W Finch St S310, Dallas, TX 75201</li>
      <li>3516 Quarry Blvd, Grand Prairie, TX 75051</li>
      <li>6437 Wexley Crest Dr, San Antonio, TX 78240</li>
      <li>5822 Ember Rd, Pasadena, TX 77504</li>
    </ul>
  </section>

  <section class="card card--front-reminder">
    <div class="brand brand--card" style="top:100px"><span class="brand-dot"></span>Bright Pelvic Health</div>
    <ul class="appointment">
      <li>DATE:<span class="fill-line"></span></li>
      <li>TIME:<span class="fill-line"></span></li>
    </ul>
    <ul class="contact">
      <li><span class="label">phone:</span> <span class="value">469-555-0172</span></li>
      <li><span class="label">fax:</span> <span class="value">1-469-555-0188</span></li>
      <li class="gap"><span class="label">email:</span> <span class="value">admin@brightpelvic.example</span></li>
      <li><span class="label">website:</span> <span class="value">www.brightpelvichealth.example</span></li>
    </ul>
  </section>

  <section class="card card--back-reminder">
    <div class="watermark" role="img" aria-label="Faint brand mark decoration">
      <span class="watermark-dot"></span>
      <span class="watermark-name">Bright Pelvic Health</span>
    </div>
    <ul class="locations">
      <li>4815 Juniper Way, Plano, TX 75093</li>
      <li>3720 Baywood Rd, Plano, TX 75025</li>
      <li>2245 Larkspur Ln, Irving, TX 75038</li>
      <li>815 W Finch St S310, Dallas, TX 75201</li>
      <li>3516 Quarry Blvd, Grand Prairie, TX 75051</li>
      <li>6437 Wexley Crest Dr, San Antonio, TX 78240</li>
      <li>5822 Ember Rd, Pasadena, TX 77504</li>
    </ul>
  </section>

  <p class="caption caption--business">Bright Pelvic Health Business Card_1</p>
  <p class="caption caption--reminder">Double-sided "appointment reminder card" Design_1</p>

</body>
</html>
```